依頼詳細
某ホテルのブライダルフェアや内覧会(結婚が決まったカップルが衣装や引き出物などを選ぶイベント)などでお客様に配布します。お客様にこのチラシを見せながら内容を説明したりもするので、わかりやすい料金とコース内容が伝えられるデザインをお願いします。
記載項目
屋号/電話番号/料金プラン/なにか良いキャッチフレーズなどあればお願いしたいです。
サイズ
A4
ページ数
片面
希望イメージ
シンプル 複雑
単色 カラフル
暗い 明るい
日常 高級
遊び心 厳粛
未来的 伝統的
女性的 男性的
希望する色
オレンジ、緑など「新鮮」「明るい」イメージ色を希望します。
納品ファイル
• イラストレーター形式 (.ai)
• フォトショップ形式 (.psd)
補足説明
いままでは市販のワープロソフトなどで付属のテンプレートなどを元に作ってきましたが、
やはりプロの広告を出している他社と大きく差がついてしまっています。 もう自分でデザインしていては他社と差が広がるばかりと感じ、今回依頼させていただきます。よろしくお願いいたします。
当方の使用していたチラシです
遅れてすみませんでした。映っている本人たちに許可は取りました。よろしくお願いいたします。
■ 選んだ理由

最終的にお二方の提案を残させていただきましたが、通り過ぎるようとするお客様の目を止まらせ、それでいて優先される物が目立ち、シンプルにまとまっていてちょっとポップな感じで同ビデオ業者との差別化をはかっているこの提案を選ばせていただきました。

■ 提案者全員のお礼・コメント

この度は当方の依頼に対して、予想以上に多くのクリエーターの方々から、想像以上にハイクオリティーな提案を多数いただき心から感謝しております。
本当にどれを選んで良い物かかなり悩みました。改めてこのサイトの素晴らしさを実感いたしました。次回また商品内容を変える際には間違いなくここに依頼させていただきます。
提案を下さったすべてのクリエーターの皆様に感謝申し上げます。
ありがとうございました。

```html
<!DOCTYPE html>
<html lang="ja">
<head>
<meta charset="utf-8">
<title>Memorial Video — ブライダル映像プラン</title>
<link href="https://fonts.googleapis.com/css2?family=Great+Vibes&family=Cinzel:wght@600&family=Noto+Serif+JP:wght@400;600&family=Noto+Sans+JP:wght@400;700&display=swap" rel="stylesheet">
<style>
:root{
  --bg:#fff8ec;
  --orange:#f08a24;
  --orange-deep:#d96a0e;
  --orange-soft:#ffe2c2;
  --green:#6aab3c;
  --green-deep:#3f7d22;
  --green-soft:#e4f2d6;
  --row:#fff0dd;
  --row-alt:#ffffff;
  --cream:#fffdf6;
  --ink:#3d3a28;
  --muted:#7b7560;
  --white:#ffffff;
}
*{margin:0;padding:0;box-sizing:border-box}
html,body{width:858px;height:1200px;overflow:hidden;background:var(--white)}
body{font-family:"Noto Sans JP",sans-serif;color:var(--ink)}
.flyer{position:relative;width:858px;height:1200px;background:var(--bg);overflow:hidden}

/* hero */
.hero{position:absolute;left:0;top:0;width:858px;height:272px;
  background:radial-gradient(ellipse at 70% 35%,#fff3d6 0%,#ffc774 30%,#f08a24 62%,#c6600c 100%)}
.hero-title{position:absolute;left:0;right:0;top:60px;text-align:center;
  font-family:"Great Vibes",cursive;font-size:104px;line-height:1;color:var(--white);
  text-shadow:0 2px 6px rgba(150,70,0,.5)}
.hero-tagline{position:absolute;left:0;right:0;top:178px;text-align:center;
  font-family:"Noto Serif JP",serif;font-size:22px;letter-spacing:.28em;color:var(--white);
  text-shadow:0 1px 4px rgba(120,50,0,.6)}
.hero-badge{position:absolute;left:718px;top:222px;width:116px;height:36px;
  background:linear-gradient(180deg,#8fcf5a,var(--green-deep));transform:rotate(-14deg);
  display:flex;align-items:center;justify-content:center;border-radius:4px;
  font-family:"Noto Serif JP",serif;font-weight:600;font-size:14px;color:var(--white)}

/* photo strips */
.strip{position:absolute;left:0;width:858px;display:flex;gap:4px;background:var(--white);padding:4px}
.strip .ph{flex:1}
.ph{background:linear-gradient(160deg,#f4a95a,#ffe6c2 55%,#e07c26)}
.ph.light{background:linear-gradient(160deg,#fff4e0,#f6c98f 60%,#fffaf0)}
.ph.green{background:linear-gradient(160deg,#8ec35e,#e3f2cf 60%,#5a9a30)}

/* sections */
.section{position:absolute;left:0;width:858px}
.label{position:absolute;left:22px;width:228px;height:108px;background:var(--cream);
  border:2px solid var(--orange);border-radius:8px;box-shadow:0 0 0 4px var(--cream),0 0 0 5px var(--green);
  display:flex;flex-direction:column;align-items:center;justify-content:center;text-align:center}
.label-en{font-family:"Great Vibes",cursive;font-size:32px;line-height:1;color:var(--orange-deep)}
.label-ja{font-family:"Noto Serif JP",serif;font-size:15px;color:var(--green-deep);margin-top:6px;line-height:1.4}
.desc{position:absolute;left:280px;width:550px;font-size:10.5px;line-height:1.65;color:var(--ink)}

.price{position:absolute;left:280px;width:550px;border-collapse:separate;border-spacing:0 3px;font-size:12.5px}
.price th{background:var(--green);color:var(--white);font-weight:700;height:24px;font-size:12px}
.price td{height:26px;background:var(--row);text-align:center}
.price tr:nth-child(even) td{background:var(--row-alt)}
.price td.item{text-align:left;padding-left:14px;font-weight:700;color:var(--green-deep)}
.price td.yen{text-align:right;padding-right:16px;font-weight:700;color:var(--orange-deep)}
.price .note{display:block;font-size:8.5px;font-weight:400;color:var(--muted)}

/* footer */
.notes{position:absolute;left:22px;top:1034px;width:814px;font-size:9px;line-height:1.6;color:var(--muted)}
.contact-bar{position:absolute;left:0;top:1072px;width:858px;height:32px;background:var(--green);
  display:flex;align-items:center;justify-content:space-between;padding:0 22px;color:var(--white)}
.studio{font-family:"Cinzel",serif;font-size:15px;color:var(--white)}
.tel{font-size:14px;font-weight:700;letter-spacing:.06em}
.hotel{position:absolute;left:0;top:1104px;width:858px;height:96px;
  background:linear-gradient(180deg,var(--orange-soft),var(--white));
  display:flex;align-items:center;justify-content:center;
  font-family:"Cinzel",serif;font-size:30px;letter-spacing:.14em;color:var(--orange-deep)}
</style>
</head>
<body>
<main class="flyer">

  <header class="hero" role="img" aria-label="花嫁のポートレートとチャペルの柔らかな光を重ねたメインビジュアル">
    <h1 class="hero-title">Memorial Video</h1>
    <p class="hero-tagline">ふたりの大切な瞬間だから感動そのままに</p>
    <div class="hero-badge">お得なプラン</div>
  </header>

  <div class="strip" style="top:272px;height:96px">
    <div class="ph light" role="img" aria-label="ウエディングドレスの新郎新婦"></div>
    <div class="ph" role="img" aria-label="披露宴会場のテーブル"></div>
    <div class="ph green" role="img" aria-label="ガーデンの挙式"></div>
    <div class="ph light" role="img" aria-label="チャペルの挙式風景"></div>
    <div class="ph" role="img" aria-label="乾杯するゲスト"></div>
    <div class="ph green" role="img" aria-label="緑の庭園"></div>
  </div>

  <section class="section" style="top:376px;height:166px">
    <div class="label" style="top:22px">
      <span class="label-en">Memorial Video</span>
      <span class="label-ja">挙式披露宴<br>メモリアルビデオ</span>
    </div>
    <p class="desc" style="top:6px">挙式・披露宴の感動を一本の作品に。プロのカメラマンが当日のすべてを丁寧に撮影し、心に残る映像として仕上げます。</p>
    <table class="price" style="top:40px">
      <tr><th></th><th>メニュー無し</th><th>メニュー有り</th></tr>
      <tr><td class="item">挙式のみ</td><td class="yen">¥ 60,000円</td><td class="yen">¥ 70,650円</td></tr>
      <tr><td class="item">披露宴のみ</td><td class="yen">¥ 100,000円</td><td class="yen">¥ 131,250円</td></tr>
      <tr><td class="item">挙式＋披露宴</td><td class="yen">¥ 136,000円</td><td class="yen">¥ 162,750円</td></tr>
    </table>
  </section>

  <div class="strip" style="top:546px;height:70px">
    <div class="ph" role="img" aria-label="ケーキ入刀の場面"></div>
    <div class="ph light" role="img" aria-label="ブーケのクローズアップ"></div>
    <div class="ph green" role="img" aria-label="入場シーン"></div>
    <div class="ph light" role="img" aria-label="花で飾られたテーブル"></div>
    <div class="ph" role="img" aria-label="指輪の交換"></div>
  </div>

  <section class="section" style="top:622px;height:150px">
    <div class="label" style="top:14px">
      <span class="label-en">End Roll Movie</span>
      <span class="label-ja">撮って出し<br>エンドロールムービー</span>
    </div>
    <p class="desc" style="top:6px">挙式から披露宴の様子をその日のうちに編集し、お開き前に上映。ゲストへの感謝の気持ちを映像で届けます。</p>
    <table class="price" style="top:42px">
      <tr><td class="item">基　本</td><td class="yen">¥ 108,000円</td></tr>
      <tr><td class="item">プラス<span class="note">メモリアルビデオと同時にお申込みの場合</span></td><td class="yen">¥ 78,750円</td></tr>
    </table>
  </section>

  <div class="strip" style="top:776px;height:82px">
    <div class="ph green" role="img" aria-label="ホテルの外観"></div>
    <div class="ph light" role="img" aria-label="ガーデンの装花"></div>
    <div class="ph" role="img" aria-label="祭壇と十字架"></div>
    <div class="ph light" role="img" aria-label="白いホテルの建物"></div>
    <div class="ph green" role="img" aria-label="ライトアップされた庭園"></div>
  </div>

  <section class="section" style="top:866px;height:164px">
    <div class="label" style="top:22px">
      <span class="label-en">Option</span>
      <span class="label-ja">追加サービス</span>
    </div>
    <table class="price" style="top:26px">
      <tr><td class="item">ハイビジョン仕上げ<span class="note">高画質ディスクでの納品となります</span></td><td class="yen">¥ 52,500円</td></tr>
      <tr><td class="item">挙式出張撮影<span class="note">館外の教会・神社での撮影</span></td><td class="yen">¥ 10,500円</td></tr>
      <tr><td class="item">ディスクコピー<span class="note">1枚あたりの料金です</span></td><td class="yen">¥ 10,500円</td></tr>
    </table>
  </section>

  <p class="notes">※ 表示価格はすべて税込です。撮影内容・編集方法のご相談はお気軽にスタッフまでお問い合わせください。お申込みは挙式日の1か月前までにお願いいたします。</p>

  <div class="contact-bar">
    <span class="studio">Atelier Studio LUMEN</span>
    <span class="tel">TEL/FAX 012-345-6789</span>
  </div>

  <footer class="hotel">HOTEL AURORA GARDEN</footer>
</main>
</body>
</html>
```